Präsentationsvorlagen für virtuelles Vertriebstraining
Zielgruppe
Ich biete virtuelles Vertriebstraining an. Das heißt ich bringe Vetriebsmannschaften bei, wie sie Videos und Online Collaboration Tools nutzen können um besser zu verkaufen.
Zielgruppe sind Firmen, die anspruchsvolle, erklärungsbedürftige Produkte im B2B Umfeld vertrieben.
Aufgabenstellung
In meinen Präsentationen arbeite ich mit relativ wenig Text und vielen Bildern.
Das Design soll sehr futuristisch und modern sein, wobei ein gewisser 80er Cyberpunk Stil durchaus willkommen ist.
Nicht zu verspielt sehr, klar. Anthrazit, Metall mit Neon Elementen.
Powerpoint Format

```html
<!DOCTYPE html>
<html lang="de">
<head>
<meta charset="utf-8">
<title>Typoblindtext – Folie</title>
<link rel="stylesheet" href="https://fonts.googleapis.com/css2?family=Montserrat:wght@300;400;500;700&display=swap">
<style>
  :root {
    --ink: #151515;
    --anthracite: #2b3033;
    --rule: #d8d6de;
    --neon-pink: #f93bd6;
    --neon-blue: #6376ff;
    --neon-cyan: #99fdfd;
    --metal: #d6d5dd;
    --paper: #ffffff;
  }
  * { margin: 0; padding: 0; box-sizing: border-box; }
  html, body { width: 1200px; height: 849px; overflow: hidden; background: var(--paper); }
  .slide {
    position: relative;
    width: 1200px;
    height: 849px;
    background: var(--paper);
    font-family: "Montserrat", sans-serif;
    color: var(--ink);
  }
  .slide-title {
    position: absolute;
    right: 215px;
    top: 42px;
    font-size: 44px;
    font-weight: 300;
    letter-spacing: 0.5px;
    color: var(--anthracite);
    line-height: 1;
  }
  .title-rule {
    position: absolute;
    left: 22px;
    top: 91px;
    width: 962px;
    height: 2px;
    background: var(--rule);
  }
  .brand {
    position: absolute;
    left: 1022px;
    top: 52px;
    display: flex;
    align-items: center;
    gap: 8px;
    font-size: 20px;
    font-weight: 500;
    color: var(--anthracite);
  }
  .brand-square { width: 12px; height: 12px; background: var(--anthracite); }
  .chart { position: absolute; left: 0; top: 0; }
  .stat {
    position: absolute;
    left: 549px;
    top: 228px;
    font-size: 86px;
    font-weight: 700;
    letter-spacing: -1px;
    line-height: 1;
  }
  .copy {
    position: absolute;
    left: 552px;
    width: 522px;
    font-size: 16px;
    line-height: 21.4px;
    text-align: justify;
    letter-spacing: 0.9px;
  }
  .copy-lead { top: 327px; font-weight: 400; }
  .copy-lead strong { font-weight: 500; }
  .copy-summary { top: 516px; font-weight: 500; letter-spacing: 0.7px; }
  .footer-band {
    position: absolute;
    left: 0;
    bottom: 0;
    width: 1200px;
    height: 24px;
    background: var(--anthracite);
  }
</style>
</head>
<body>
<main class="slide">
  <h1 class="slide-title">TYPOBLINDTEXT</h1>
  <div class="title-rule"></div>
  <div class="brand"><span class="brand-square"></span>Salterno</div>

  <svg class="chart" width="1200" height="849" viewBox="0 0 1200 849" role="img" aria-label="Kreisdiagramm mit 65 Prozent Hauptanteil">
    <path fill="var(--neon-pink)" d="M305 426 L305 246 A180 180 0 1 1 244 595 Z"/>
    <path fill="var(--neon-blue)" d="M305 426 L244 595 A180 180 0 0 1 128 396 Z"/>
    <path fill="var(--neon-cyan)" d="M305 426 L128 396 A180 180 0 0 1 189 289 Z"/>
    <path fill="var(--metal)" d="M305 426 L189 289 A180 180 0 0 1 305 246 Z"/>
  </svg>

  <div class="stat">65%</div>

  <p class="copy copy-lead"><strong>Dies ist ein Typoblindtext.</strong> An ihm kann man sehen, ob alle Buchstaben da sind und wie sie aussehen. Manchmal benutzt man Worte wie Hamburgefonts, Rafgenduks oder Handgloves, um Schriften zu testen. Manchmal Sätze, die alle Buchstaben des Alphabets enthalten - man nennt diese Sätze »Pangrams«. Sehr bekannt ist dieser: The quick brown fox jumps over the lazy old dog. Oft werden in Typoblindtexte auch fremdsprachige Worte benutzt.</p>

  <p class="copy copy-summary">Dies ist ein Typoblindtext. An ihm kann man sehen, ob alle Buchstaben da sind und wie sie aussehen. Manchmal benutzt man Worte wie Hamburgefonts, Rafgenduks oder Handgloves, um Schriften zu testen.</p>

  <div class="footer-band"></div>
</main>
</body>
</html>
```